Cradle Glow Events

New Company ,I will attened clients personal residents(venu of there choice) and provide 3D ultra sound photos at time of ultra sound.This is a Non diagnostic ultra sound which does not replace the ultrasound reqested by Dr.The best time for ultra sound is 24 to 34 weeks.The baby sex can be kept confidential if requied and all cultral and diverse backgrounds cattered for..No referal requied for this.I have 2 main packges,1 baby shower and 2 family time.Extra options available are entertainment,Family time prior to baby shower for dad,decoration, Kids entertainment.
Contact number is 0471938402 email to be added ASAP.
prices start from $450

It Company

```html
<!DOCTYPE html>
<html lang="en">
<head>
<meta charset="utf-8">
<title>Cradle Glow Events – Flyer</title>
<link href="https://fonts.googleapis.com/css2?family=Chewy&family=Arimo:wght@400;700&display=swap" rel="stylesheet">
<style>
  :root {
    --magenta: #d6175c;
    --plum: #a3185e;
    --orange: #f7862a;
    --orange-soft: #fbc58f;
    --teal-soft: #d9eeee;
    --teal: #9fcfcf;
    --ink: #3f3f3f;
    --white: #ffffff;
    --glow: #9ff3ee;
  }
  html, body { margin: 0; padding: 0; overflow: hidden; background: var(--white); }
  .flyer {
    position: relative; width: 1200px; height: 2437px; overflow: hidden;
    background: var(--white);
    font-family: "Arimo", Arial, sans-serif;
  }
  .backdrop { position: absolute; inset: 0; }
  .badge {
    position: absolute; left: 890px; top: -70px; width: 340px; height: 340px;
  }
  .badge-label {
    position: absolute; left: 950px; top: 50px; width: 240px;
    transform: rotate(38deg); text-align: center;
    font-family: "Chewy", cursive; font-size: 44px; line-height: 1; color: var(--white);
    letter-spacing: 2px;
  }
  .brand {
    position: absolute; left: 80px; top: 390px; width: 1040px;
    font-family: "Chewy", cursive; color: var(--magenta);
    font-size: 150px; line-height: 1.02; text-align: center;
  }
  .headline {
    position: absolute; left: 40px; top: 865px; width: 1120px; text-align: center;
    font-family: "Chewy", cursive; font-size: 74px; line-height: 1.05; color: var(--magenta);
    -webkit-text-stroke: 3px var(--white); paint-order: stroke fill;
    text-shadow: 0 0 18px var(--glow), 0 0 30px var(--glow);
  }
  .disclaimer {
    position: absolute; left: 138px; top: 1082px; font-size: 30px; line-height: 1.5; color: var(--ink);
  }
  .packages-title {
    position: absolute; left: 172px; top: 1205px;
    font-family: "Chewy", cursive; font-size: 66px; color: var(--orange);
    -webkit-text-stroke: 3px var(--white); paint-order: stroke fill;
    text-shadow: 0 0 16px #fff2a8, 0 0 26px #fde6a0;
  }
  .package { position: absolute; left: 150px; display: flex; align-items: center; }
  .package-number {
    width: 78px; height: 78px; border-radius: 50%; border: 7px solid var(--orange);
    background: var(--white); box-shadow: 7px 7px 0 var(--teal);
    font-family: "Chewy", cursive; font-size: 54px; color: var(--magenta);
    display: flex; align-items: center; justify-content: center; margin-right: 76px;
  }
  .package-name {
    font-family: "Chewy", cursive; font-size: 76px; color: var(--magenta);
    -webkit-text-stroke: 3px var(--white); paint-order: stroke fill;
  }
  .package.shower { top: 1387px; }
  .package.family { top: 1548px; }
  .extras { position: absolute; left: 176px; top: 1718px; color: var(--plum); }
  .extras-heading, .extras-item { font-family: "Chewy", cursive; font-size: 50px; line-height: 1.18; }
  .extras-note { font-size: 31px; line-height: 1.25; color: var(--ink); }
  .contact {
    position: absolute; left: 176px; top: 2040px; display: flex; align-items: baseline;
    font-family: "Chewy", cursive; color: var(--plum);
  }
  .contact-label { font-size: 50px; margin-right: 26px; }
  .contact-phone { font-size: 76px; color: var(--magenta); letter-spacing: 2px; }
  .price { position: absolute; left: 177px; top: 2222px; font-size: 35px; font-weight: 700; color: var(--orange); }
</style>
</head>
<body>
<main class="flyer">
  <svg class="backdrop" width="1200" height="2437" viewBox="0 0 1200 2437" aria-hidden="true">
    <defs>
      <linearGradient id="sky" x1="0" y1="0" x2="0" y2="1">
        <stop offset="0" stop-color="#e4f3f3"/>
        <stop offset="0.45" stop-color="#f4fbfb"/>
        <stop offset="1" stop-color="#ffffff"/>
      </linearGradient>
      <linearGradient id="orangeBand" x1="0" y1="0" x2="1" y2="0">
        <stop offset="0" stop-color="#fde3cc"/>
        <stop offset="0.5" stop-color="#fcc08a"/>
        <stop offset="1" stop-color="#f77f22"/>
      </linearGradient>
      <linearGradient id="tealBand" x1="0" y1="0" x2="1" y2="0">
        <stop offset="0" stop-color="#a9d4d2"/>
        <stop offset="1" stop-color="#e7f4f3"/>
      </linearGradient>
    </defs>
    <rect width="1200" height="1300" fill="url(#sky)"/>
    <g fill="#ffffff" opacity="0.7">
      <ellipse cx="330" cy="150" rx="220" ry="110"/>
      <ellipse cx="820" cy="170" rx="200" ry="120"/>
      <ellipse cx="160" cy="820" rx="260" ry="90"/>
      <ellipse cx="1020" cy="900" rx="240" ry="100"/>
    </g>
    <rect x="0" y="820" width="1200" height="230" fill="#e3f5f4" opacity="0.8"/>
    <path d="M120 1355 Q600 1240 1070 1290 L1060 1320 Q600 1280 130 1380 Z" fill="#e5f1f1"/>
    <path d="M0 1600 Q560 1180 1200 1420 L1200 1600 Q620 1420 180 1840 Q60 1720 0 1700 Z" fill="url(#orangeBand)" opacity="0.9"/>
    <path d="M0 1760 Q300 1600 640 1660 Q940 1700 1200 1830 L1200 1900 Q900 1760 620 1730 Q300 1710 0 2000 Z" fill="url(#tealBand)" opacity="0.8"/>
    <path d="M0 2437 L0 2240 Q500 1960 1200 2000 L1200 2437 Z" fill="#f1f8f8"/>
  </svg>

  <svg class="badge" viewBox="0 0 340 340" aria-hidden="true">
    <polygon fill="var(--orange-soft)" opacity="0.9"
      points="170,0 200,95 290,50 245,140 340,170 245,200 290,290 200,245 170,340 140,245 50,290 95,200 0,170 95,140 50,50 140,95"/>
  </svg>
  <div class="badge-label">NEW<br>COMPANY</div>

  <h1 class="brand">Cradle Glow<br>Events</h1>

  <h2 class="headline">We provide unique 3D Ultra sound<br>photos at time of ultra sound.</h2>

  <p class="disclaimer">This is a Non diagnostic ultra sound<br>which does not replace the ultrasound requested by Dr.</p>

  <h3 class="packages-title">We offer 2 main packages</h3>

  <div class="package shower">
    <span class="package-number">1</span>
    <span class="package-name">baby shower &amp;</span>
  </div>
  <div class="package family">
    <span class="package-number">2</span>
    <span class="package-name">family time.</span>
  </div>

  <section class="extras">
    <div class="extras-heading">Extra options available are:</div>
    <div class="extras-item">entertainment.</div>
    <div class="extras-note">Family time prior to baby shower for dad<br>decoration.</div>
    <div class="extras-item">Kids entertainment.</div>
  </section>

  <div class="contact">
    <span class="contact-label">Call us now on:</span>
    <span class="contact-phone">047 193 8402</span>
  </div>

  <p class="price">prices start from $450</p>
</main>
</body>
</html>
```